Business Card design

I need a business card to represent my service business.

I provide a service for 3D Scanning, Reverse Engineering, 3D Design, 2D Drafting and 3D Printing.

I need my contact details on the card.
Name: Marcus Feltley
Mobile: 0471856230
Email: marcus@tmvisions.com.au

I would like QR Codes to my lumigrid and pixora pages. Please show the platform logo.
https://www.lumigrid.com/profile.php?id=100057214883902
https://www.pixora.com/tm_visions/

I am open to having a single or double sided card.

My logo text is VOX BOLD
The hex code for the green is 8dc63f

```html
<!DOCTYPE html>
<html lang="en">
<head>
<meta charset="utf-8">
<title>TM Visions – Business Card</title>
<link rel="stylesheet" href="https://fonts.googleapis.com/css2?family=Russo+One&family=Roboto:wght@400;500&display=swap">
<style>
  :root {
    --backdrop: #2c2c2c;
    --card-light: #f1f1f1;
    --card-shade: #d9d9d9;
    --brand-green: #80b83e;
    --mark-dark: #1b1b1b;
    --wordmark-grey: #6b6b6d;
    --ink: #111111;
    --strip-grey: #6f6f71;
  }
  * { margin: 0; padding: 0; box-sizing: border-box; }
  html, body { width: 1200px; height: 1138px; overflow: hidden; background: var(--backdrop); }
  body { position: relative; font-family: "Roboto", sans-serif; }

  .card {
    position: absolute;
    width: 620px;
    height: 375px;
    border-radius: 16px;
    overflow: hidden;
    background: linear-gradient(180deg, var(--card-light) 0%, #ececec 55%, var(--card-shade) 100%);
  }
  .card--front { left: 272px; top: 184px; }
  .card--back  { left: 274px; top: 606px; }

  .brand-disc {
    position: absolute;
    border-radius: 50%;
    background: var(--mark-dark);
  }
  .card--front .brand-disc { left: 234px; top: 42px; width: 156px; height: 134px; }
  .card--back  .brand-disc { left: 90px;  top: 101px; width: 120px; height: 103px; }

  .wordmark {
    position: absolute;
    font-family: "Russo One", sans-serif;
    color: var(--wordmark-grey);
    white-space: nowrap;
    transform: translateX(-50%);
    letter-spacing: 1px;
  }
  .card--front .wordmark { left: 312px; top: 178px; font-size: 44px; }
  .card--back  .wordmark { left: 150px; top: 206px; font-size: 32px; }

  .service-band {
    position: absolute;
    left: 0; top: 255px;
    width: 100%; height: 64px;
    background: var(--brand-green);
    font-family: "Russo One", sans-serif;
    font-size: 17px;
    color: var(--ink);
    text-align: center;
    line-height: 23px;
    padding-top: 9px;
  }
  .service-band .divider { margin: 0 12px; }

  .social-row {
    position: absolute;
    left: 0; top: 333px;
    width: 100%;
    display: flex;
    justify-content: center;
    align-items: center;
    gap: 8px;
    font-size: 16px;
    color: #222;
  }
  .social-row .platform { display: flex; align-items: center; gap: 6px; font-weight: 500; }
  .social-row .platform-dot { width: 16px; height: 16px; border-radius: 50%; }
  .social-row .platform--lumigrid .platform-dot { background: #1d5fa8; }
  .social-row .platform--pixora .platform-dot { background: #b8327a; }
  .social-row .handle { margin-right: 16px; }
  .social-row .handle:last-child { margin-right: 0; }

  .holder-name {
    position: absolute;
    left: 328px; top: 110px;
    font-family: "Russo One", sans-serif;
    font-size: 29px;
    color: var(--brand-green);
    letter-spacing: 0.5px;
  }
  .contact-list { position: absolute; left: 336px; top: 158px; list-style: none; }
  .contact-list li {
    display: flex; align-items: center;
    height: 24px;
    font-size: 16px;
    color: var(--ink);
  }
  .contact-list svg { width: 14px; height: 14px; margin-right: 10px; flex: none; }

  .footer-strip {
    position: absolute;
    left: 0; bottom: 0;
    width: 100%; height: 47px;
  }
  .footer-strip svg { display: block; width: 100%; height: 100%; }
  .footer-tagline {
    position: absolute;
    left: 328px; top: 338px;
    font-size: 16px;
    color: var(--ink);
  }
</style>
</head>
<body>

  <section class="card card--front">
    <div class="brand-disc"></div>
    <div class="wordmark">TM Visions</div>
    <div class="service-band">
      <div>3D Design<span class="divider">|</span>3d Scanning<span class="divider">|</span>Reverse Engineering</div>
      <div>2D Drafting and 3D Printing</div>
    </div>
    <div class="social-row">
      <span class="platform platform--lumigrid"><span class="platform-dot"></span>lumigrid</span>
      <span class="handle">/profile.php?id=100057214883902</span>
      <span class="platform platform--pixora"><span class="platform-dot"></span>pixora</span>
      <span class="handle">/tm_visions</span>
    </div>
  </section>

  <section class="card card--back">
    <div class="brand-disc"></div>
    <div class="wordmark">TM Visions</div>

    <div class="holder-name">Marcus Feltley</div>
    <ul class="contact-list">
      <li>
        <svg viewBox="0 0 14 14" aria-hidden="true"><path fill="#80b83e" d="M1 4.5c0-2 2.5-3 6-3s6 1 6 3v1h-3v-1H4v1H1z M3 6.5h8l1.5 5.5h-11z"/><circle cx="7" cy="9" r="1.6" fill="#f1f1f1"/></svg>
        0471856230
      </li>
      <li>
        <svg viewBox="0 0 14 14" aria-hidden="true"><rect x="0.5" y="2.5" width="13" height="9" fill="#80b83e"/><path d="M0.8 2.8 7 8 13.2 2.8 M0.8 11.2 5.2 6.5 M13.2 11.2 8.8 6.5" stroke="#f1f1f1" stroke-width="1" fill="none"/></svg>
        marcus@tmvisions.com.au
      </li>
      <li>
        <svg viewBox="0 0 14 14" aria-hidden="true"><circle cx="7" cy="7" r="6" fill="none" stroke="#80b83e" stroke-width="1.4"/><ellipse cx="7" cy="7" rx="2.6" ry="6" fill="none" stroke="#80b83e" stroke-width="1.2"/><path d="M1 7h12 M2 4h10 M2 10h10" stroke="#80b83e" stroke-width="1.1"/></svg>
        www.tmvisions.com.au
      </li>
    </ul>

    <div class="footer-strip">
      <svg viewBox="0 0 620 47" preserveAspectRatio="none" aria-hidden="true">
        <rect x="0" y="33" width="620" height="14" fill="#6f6f71"/>
        <polygon points="294,0 620,0 620,47 280,47" fill="#80b83e"/>
        <polygon points="294,0 620,0 620,47 262,47" fill="#80b83e"/>
      </svg>
    </div>
    <div class="footer-tagline">3D Design &amp; Laser Scanning</div>
  </section>

</body>
</html>
```